Refresh of Business Card Design

Want to refresh the business card design with the new logo while adhering to style guide as attached. Would like to match feel of website www.durmackvinex.com

```html
<!DOCTYPE html>
<html lang="en">
<head>
<meta charset="utf-8">
<title>Durmack Vinex – Business Card</title>
<link href="https://fonts.googleapis.com/css2?family=Montserrat:wght@400;500;700&display=swap" rel="stylesheet">
<style>
  :root {
    --backdrop: #3a3a3c;
    --card-white: #ffffff;
    --card-black: #141414;
    --brand-red: #d9202a;
    --ink: #1a1a1a;
  }
  * { box-sizing: border-box; margin: 0; padding: 0; }
  html, body { width: 1200px; height: 1200px; overflow: hidden; }
  body {
    background: var(--backdrop);
    font-family: "Montserrat", sans-serif;
    position: relative;
  }
  .card {
    position: absolute;
    left: 150px;
    width: 900px;
    height: 514px;
    border-radius: 40px;
    overflow: hidden;
  }
  .card-front { top: 60px; background: var(--card-white); }
  .card-back { top: 626px; background: var(--card-black); }

  .front-bands { position: absolute; inset: 0; width: 900px; height: 514px; }

  .identity { position: absolute; left: 56px; top: 176px; }
  .full-name {
    color: var(--brand-red);
    font-weight: 700;
    font-size: 54px;
    letter-spacing: 1px;
    line-height: 1;
  }
  .position {
    color: var(--ink);
    font-weight: 500;
    font-size: 24px;
    letter-spacing: 1px;
    margin-top: 4px;
  }
  .contact-list { list-style: none; margin-top: 20px; }
  .contact-item {
    display: flex;
    align-items: flex-start;
    gap: 14px;
    color: var(--ink);
    font-size: 20px;
    line-height: 1.25;
    margin-bottom: 7px;
  }
  .contact-icon { width: 22px; height: 22px; flex: none; margin-top: 2px; }

  .brand-mark {
    position: absolute;
    display: flex;
    align-items: center;
    gap: 16px;
    font-weight: 700;
    letter-spacing: 2px;
  }
  .brand-mark .dot { border-radius: 50%; background: var(--brand-red); flex: none; }
  .brand-front { right: 60px; top: 100px; color: var(--ink); font-size: 30px; }
  .brand-front .dot { width: 56px; height: 56px; }
  .brand-back {
    left: 50%; top: 50%;
    transform: translate(-50%, -50%);
    color: var(--card-white);
    font-size: 46px;
    white-space: nowrap;
  }
  .brand-back .dot { width: 84px; height: 84px; }
</style>
</head>
<body>

<section class="card card-front" aria-label="Business card front">
  <svg class="front-bands" viewBox="0 0 900 514" aria-hidden="true">
    <polygon points="0,496 570,460 570,514 0,514" fill="var(--brand-red)"/>
    <polygon points="584,458 900,420 900,514 584,514" fill="var(--card-black)"/>
  </svg>

  <div class="brand-mark brand-front">
    <span class="dot"></span>
    <span class="brand-name">DURMACK VINEX</span>
  </div>

  <div class="identity">
    <h1 class="full-name">FULL NAME</h1>
    <p class="position">POSITION</p>
    <ul class="contact-list">
      <li class="contact-item">
        <svg class="contact-icon" viewBox="0 0 24 24" aria-hidden="true"><rect x="6" y="1.5" width="12" height="21" rx="2" fill="none" stroke="var(--brand-red)" stroke-width="2"/><circle cx="12" cy="19" r="1.3" fill="var(--brand-red)"/></svg>
        <span>806.555.0142</span>
      </li>
      <li class="contact-item">
        <svg class="contact-icon" viewBox="0 0 24 24" aria-hidden="true"><rect x="1.5" y="5" width="21" height="14" fill="var(--brand-red)"/><polyline points="1.5,5 12,13 22.5,5" fill="none" stroke="#fff" stroke-width="1.6"/></svg>
        <span>jdale@durmackvinex.com</span>
      </li>
      <li class="contact-item">
        <svg class="contact-icon" viewBox="0 0 24 24" aria-hidden="true"><g fill="none" stroke="var(--brand-red)" stroke-width="1.8"><circle cx="12" cy="12" r="10"/><ellipse cx="12" cy="12" rx="4.5" ry="10"/><line x1="2" y1="12" x2="22" y2="12"/><line x1="4" y1="6.5" x2="20" y2="6.5"/><line x1="4" y1="17.5" x2="20" y2="17.5"/></g></svg>
        <span>www.durmackvinex.com</span>
      </li>
      <li class="contact-item">
        <svg class="contact-icon" viewBox="0 0 24 24" aria-hidden="true"><path d="M12 23s-8-8.5-8-14a8 8 0 0 1 16 0c0 5.5-8 14-8 14z" fill="var(--brand-red)"/><circle cx="12" cy="9" r="3" fill="#fff"/></svg>
        <span>P.O. Box 52190 Carrow, TX 79702<br>48 Ridgeline Ave Hollin, Texas 79120</span>
      </li>
    </ul>
  </div>
</section>

<section class="card card-back" aria-label="Business card back">
  <div class="brand-mark brand-back">
    <span class="dot"></span>
    <span class="brand-name">DURMACK VINEX</span>
  </div>
</section>

</body>
</html>
```